A design led business card for the construction industry

High-end business card to match logo. White logo on dark grey/off black to the front. Matching dark font on white to back, possibly with logo design again.

We offer construction and project management services to commercial and private clients in the UK. Projetcs range from newbuilds, conversion of listed buildings and refurbishments and extensions of existing homes. Our focus is on quality and attention to detail using the highest skills.

Contact Information for Business Card

Name; Dorian Hatch BSc
Position; Project Manager
Mobile; 07962 804 157
Tel; 01632 958412
email; dorian@framelark.co.uk
web; www.framelark.co.uk
Address; Ashcombe on Wey, KT4 7PZ

Colors

Designer to choose only greyscale colors for use in the design.

Requirements
Must have
• To include the below description of the business,

CONSTRUCTION - PROJECT MANAGEMENT
Nice to have
• The posibility of the top back of the card being used as a ruler. So will have a measurement to scale in mm or an architect scale of 1:50
Should not have
• Should not be portrait

```html
<!DOCTYPE html>
<html lang="en">
<head>
<meta charset="utf-8">
<title>Framelark business card</title>
<link href="https://fonts.googleapis.com/css2?family=Arimo:wght@400;700&display=swap" rel="stylesheet">
<style>
  :root {
    --backdrop: #666666;
    --card-light: #f1eff0;
    --card-dark: #121212;
    --ink-light: #ffffff;
    --ink-dark: #111111;
    --ink-muted: #8a8a8a;
    --ink-brand-dark: #3a3a3a;
  }
  * { margin: 0; padding: 0; box-sizing: border-box; }
  html, body {
    width: 1200px; height: 801px; overflow: hidden;
    background: var(--backdrop);
    font-family: "Arimo", Arial, sans-serif;
  }
  .canvas { position: relative; width: 1200px; height: 801px; }

  .card { position: absolute; border-radius: 7px; overflow: hidden; }
  .card--front { left: 371px; top: 90px; width: 441px; height: 262px; background: var(--card-light); }
  .card--back { left: 371px; top: 394px; width: 443px; height: 263px; background: var(--card-dark); }

  .brand-block {
    position: absolute; left: 18px; top: 22px; width: 117px; height: 222px;
    display: flex; flex-direction: column; align-items: center; justify-content: center; gap: 14px;
  }
  .brand-block__square { width: 44px; height: 44px; background: var(--ink-dark); }
  .brand-block__name {
    font-weight: 700; font-size: 14px; letter-spacing: 1.5px; color: var(--ink-dark);
  }

  .contact-panel {
    position: absolute; left: 154px; top: 41px; width: 255px; height: 180px;
    background: var(--ink-dark); color: var(--ink-light);
  }
  .contact-panel__pointer { position: absolute; left: -20px; top: 73px; }
  .contact-panel__body { position: absolute; left: 27px; top: 27px; }

  .person__name { font-size: 14.5px; font-weight: 700; line-height: 17px; }
  .person__name span { font-weight: 400; }
  .person__role { font-size: 13px; line-height: 15px; }

  .contact-list { list-style: none; margin-top: 12px; }
  .contact-list li {
    display: flex; align-items: center; gap: 4px;
    font-size: 13px; line-height: 15.6px;
  }
  .contact-list svg { width: 11px; height: 11px; flex: none; }
  .address { font-size: 13px; margin-top: 12px; }

  .back-brand {
    position: absolute; left: 0; right: 0; top: 160px; text-align: center;
    font-size: 20px; letter-spacing: 15px; padding-left: 15px;
    color: var(--ink-brand-dark);
  }
  .back-tagline {
    position: absolute; left: 0; right: 0; top: 197px; text-align: center;
    font-size: 11px; color: var(--ink-muted); letter-spacing: 0.2px;
  }
</style>
</head>
<body>
<main class="canvas">

  <section class="card card--front" aria-label="Card front">
    <div class="brand-block">
      <div class="brand-block__square"></div>
      <div class="brand-block__name">FRAMELARK</div>
    </div>

    <div class="contact-panel">
      <svg class="contact-panel__pointer" width="21" height="40" viewBox="0 0 21 40">
        <polygon points="21,0 0,20 21,40" fill="#111111"/>
      </svg>
      <div class="contact-panel__body">
        <p class="person__name">DORIAN HATCH <span>BSc</span></p>
        <p class="person__role">Project Manager</p>

        <ul class="contact-list">
          <li>
            <svg viewBox="0 0 12 12"><rect x="3" y="0.8" width="6" height="10.4" rx="1" fill="none" stroke="#fff" stroke-width="1.2"/><line x1="5" y1="9.3" x2="7" y2="9.3" stroke="#fff"/></svg>
            07962 804 157
          </li>
          <li>
            <svg viewBox="0 0 12 12"><path d="M2.5 1 L4.5 1 L5.3 3.6 L4 4.6 Q5 7 7.4 8 L8.4 6.7 L11 7.5 L11 9.5 Q10.5 11 9 11 Q1 10 1 2.5 Q1 1 2.5 1 Z" fill="none" stroke="#fff" stroke-width="1.1"/></svg>
            01632 958412
          </li>
          <li>
            <svg viewBox="0 0 12 12"><rect x="0.5" y="2.5" width="11" height="7.5" fill="#fff"/><polyline points="0.5,2.5 6,7 11.5,2.5" fill="none" stroke="#111" stroke-width="1"/></svg>
            dorian@framelark.co.uk
          </li>
          <li>
            <svg viewBox="0 0 12 12" fill="none" stroke="#fff" stroke-width="0.9"><circle cx="6" cy="6" r="5.2"/><ellipse cx="6" cy="6" rx="2.2" ry="5.2"/><line x1="0.8" y1="6" x2="11.2" y2="6"/><line x1="1.6" y1="3.3" x2="10.4" y2="3.3"/><line x1="1.6" y1="8.7" x2="10.4" y2="8.7"/></svg>
            www.framelark.co.uk
          </li>
        </ul>
        <p class="address">Ashcombe on Wey, KT4 7PZ</p>
      </div>
    </div>
  </section>

  <section class="card card--back" aria-label="Card back">
    <p class="back-brand">FRAMELARK</p>
    <p class="back-tagline">CONSTRUCTION - PROJECT MANAGEMENT</p>
  </section>

</main>
</body>
</html>
```